Email marketing for Brightfield Optic Services

I need nice design brochure for e mail marketing telling my customers our services and products, location, etc.
At Brightfield Optic Services, we have 25 plus years of combined experience servicing ophthalmic equipment. We offer reliable, timely and economic repairs of a variety of new and discontinued equipment, including, but not limited to Exam Chairs and Stands, Phoropters, Slit Lamps, Keratometers, Hand-helds, BIO’s, Auto Lensmeters, AutoRefractors, Non-Contact Tonometers, Goldman Tonometers, Vira-Tips and many more.

We service all major brands such as: Vell Dorran, Tilsa, Quaven, Fendworth, Ulmbrook, Parsivel, Kessig and more.
We do Preventative Maintenance, Practice Moving, Office Relocation Consulting, Layout Strategy and Equipment Set Up Solutions.

Target Market(s)

Optometrist, Ophthalmologists, Optical Stores

Font styles to use
Sans Serif

Colors
34a6d7

Requirements
Must have
• We comply with all the safety measure according to BHA. Emphasize more on services, service calls.
Link to my website www.brightfieldoptic.example
We buy, sale and service ophthalmic equipment.
Phoroptor cleaning only 275.00. Please use file 4.
File 3 special price for a limited time 925.00.
File 1, Refractor Breath Shield- 19.00.
File 2, Slit Lamp Breath Shield XL 17.00
Nice to have
• I want nice looking professional design that also assures my customers that we are open for business, we comply with all the safety guidelines.

```html
<!DOCTYPE html>
<html lang="en">
<head>
<meta charset="utf-8">
<title>Brightfield Optic Services – Email</title>
<link rel="stylesheet" href="https://fonts.googleapis.com/css2?family=Barlow:wght@300;400;500;600;700&family=Rubik:wght@400&display=swap">
<style>
:root{
  --backdrop:#2b2b2b;
  --navy:#1e2a78;
  --blue:#34a6d7;
  --blue-dark:#2c8fc0;
  --ink:#3c3c3c;
  --grey-text:#555;
  --rule:#e6e6e6;
  --panel:#eaf3fd;
  --footer-bar:#4a4a4a;
  --white:#fff;
}
*{margin:0;padding:0;box-sizing:border-box}
html,body{width:1200px;height:3520px;overflow:hidden;background:var(--backdrop)}
body{font-family:"Barlow",Arial,sans-serif;color:var(--ink);position:relative}
.email{position:absolute;left:73px;top:66px;width:1048px;height:3381px;background:var(--white);overflow:hidden}
.abs{position:absolute}
.notice{left:0;top:0;width:100%;height:84px;display:flex;align-items:center;justify-content:center;color:var(--navy);font-size:21px;font-weight:500}
.masthead{left:0;top:84px;width:100%;height:132px;background:var(--navy);display:flex;flex-direction:column;align-items:center;justify-content:center;color:var(--white);font-weight:400;letter-spacing:3px;line-height:1.15}
.masthead .brand-main{font-size:34px}
.masthead .brand-sub{font-size:28px;letter-spacing:8px}
.hero-photo{left:0;top:216px;width:100%;height:477px;background:linear-gradient(110deg,#1c2f4a 0%,#39557a 30%,#8fb0cf 60%,#d9e6f1 100%)}
.headline-band{left:0;top:693px;width:100%;height:193px;background:var(--blue);color:var(--white);text-align:center}
.headline-band h1{font-size:68px;font-weight:700;line-height:1;margin-top:32px;letter-spacing:1px}
.headline-band h2{font-size:46px;font-weight:300;line-height:1;margin-top:12px;letter-spacing:1px}
.intro{left:60px;top:920px;width:928px;text-align:center;font-family:"Rubik",Arial,sans-serif;font-size:22px;line-height:49px;color:var(--grey-text)}
.section-title{left:0;top:1188px;width:100%;height:56px}
.section-title .label{position:absolute;left:0;width:100%;text-align:center;top:0;font-size:39px;font-weight:600;color:var(--blue)}
.section-title .line{position:absolute;top:27px;height:3px;background:var(--blue)}
.section-title .dot{position:absolute;top:21px;width:14px;height:14px;border-radius:50%;background:var(--blue)}
.offer-grid{left:0;top:1262px;width:100%;height:1198px}
.grid-v{position:absolute;left:526px;top:0;width:2px;height:1198px;background:var(--rule)}
.grid-h{position:absolute;left:0;top:599px;width:100%;height:2px;background:var(--rule)}
.offer{position:absolute;width:524px;height:599px;text-align:center}
.offer .ring{position:absolute;left:110px;top:16px;width:318px;height:318px;border:3px solid var(--blue);border-radius:50%}
.offer .photo{position:absolute;left:8px;top:8px;width:296px;height:296px;border-radius:50%}
.offer .badge{position:absolute;left:236px;top:212px;width:108px;height:108px;border-radius:50%;background:var(--blue);border:5px solid var(--white);box-shadow:0 0 0 2px var(--blue);color:var(--white);display:flex;flex-direction:column;align-items:center;justify-content:center;font-size:25px;line-height:1.1}
.offer h3{position:absolute;left:0;width:100%;top:412px;font-size:30px;font-weight:600;color:var(--blue)}
.offer p{position:absolute;left:0;width:100%;top:456px;font-size:23px;line-height:34px;color:var(--ink)}
.offer .more{position:absolute;left:0;width:100%;top:528px;font-size:22px;color:var(--blue)}
.other-services{left:0;top:2520px;width:100%;text-align:center}
.other-services h4{font-size:30px;font-weight:600;color:var(--blue)}
.tick-list{display:flex;flex-wrap:wrap;justify-content:center;gap:0 30px;font-size:24px;color:var(--ink);list-style:none}
.tick-list li{display:flex;align-items:center;gap:10px;height:50px}
.tick-list svg{width:26px;height:26px}
.other-services .tick-list{margin:22px auto 0;width:960px}
.brands{left:0;top:2738px;width:100%;height:322px;background:var(--panel);text-align:center}
.brands h4{font-size:40px;font-weight:500;color:var(--blue);margin-top:70px}
.brands .tick-list{width:780px;margin:22px auto 0;font-size:27px;gap:0 24px}
.footer{left:0;top:3060px;width:100%;height:274px;background:var(--blue);color:var(--white);font-size:23px;line-height:35px}
.footer .location{position:absolute;right:530px;top:50px;text-align:right}
.footer .timing{position:absolute;left:582px;top:50px}
.footer b{font-weight:700}
.copyright{left:0;top:3334px;width:100%;height:47px;background:var(--footer-bar);color:var(--white);font-size:21px;display:flex;align-items:center;justify-content:center}
</style>
</head>
<body>
<svg width="0" height="0" style="position:absolute">
  <symbol id="tick" viewBox="0 0 26 26">
    <rect x="2" y="6" width="17" height="17" fill="none" stroke="#34a6d7" stroke-width="2"/>
    <path d="M6 13 l5 5 L24 3" fill="none" stroke="#34a6d7" stroke-width="3.2" stroke-linecap="round" stroke-linejoin="round"/>
  </symbol>
</svg>

<main class="email">
  <div class="abs notice">We are open for business, we comply with all the safety guidelines.</div>

  <header class="abs masthead">
    <span class="brand-main">BRIGHTFIELD OPTIC</span>
    <span class="brand-sub">SERVICES</span>
  </header>

  <div class="abs hero-photo" role="img" aria-label="Close-up photograph of ophthalmic microscope eyepieces in cool blue light"></div>

  <section class="abs headline-band">
    <h1>WE BUY, SALE AND SERVICE</h1>
    <h2>OPHTHALMIC EQUIPMENT</h2>
  </section>

  <p class="abs intro">At Brightfield Optic Services, we have 25 plus years of combined experience servicing ophthalmic equipment. We offer reliable, timely and economic repairs of a variety of new and discontinued equipment, including, but not limited to Exam Chairs and Stands, Phoropters, Slit Lamps, Keratometers, Hand-helds, BIO’s, Auto Lensmeters, AutoRefractors, Non-Contact Tonometers, Goldman Tonometers, Vira-Tips and many more.</p>

  <div class="abs section-title">
    <span class="line" style="left:0;width:238px"></span><span class="dot" style="left:238px"></span>
    <span class="dot" style="left:796px"></span><span class="line" style="left:810px;width:238px"></span>
    <span class="label">Brightfield Optic Services</span>
  </div>

  <section class="abs offer-grid">
    <div class="grid-v"></div><div class="grid-h"></div>

    <article class="offer" style="left:0;top:0">
      <div class="ring"><div class="photo" role="img" aria-label="Disassembled phoropter parts laid out on white" style="background:radial-gradient(circle,#d8d8d8,#f3f3f3 70%)"></div></div>
      <div class="badge"><span>Only</span><span>275.00</span></div>
      <h3>Phoroptor cleaning</h3>
      <p>Lorem ipsum is a placeholder<br>text commonly used to...</p>
      <a class="more">Read More..</a>
    </article>

    <article class="offer" style="left:528px;top:0">
      <div class="ring"><div class="photo" role="img" aria-label="Front view of a phoropter refractor head" style="background:radial-gradient(circle,#6a6a6a,#b7a58a 75%)"></div></div>
      <div class="badge"><span>Only</span><span>925.00</span></div>
      <h3>Special price for a limited time</h3>
      <p>Lorem ipsum is a placeholder<br>text commonly used to...</p>
      <a class="more">Read More..</a>
    </article>

    <article class="offer" style="left:0;top:601px">
      <div class="ring"><div class="photo" role="img" aria-label="Monitor showing refractor breath shield products" style="background:radial-gradient(circle,#e9e9e9,#f6f6f6 70%)"></div></div>
      <div class="badge"><span>Only</span><span>19.00</span></div>
      <h3>Refractor Breath Shield</h3>
      <p>Lorem ipsum is a placeholder<br>text commonly used to...</p>
      <a class="more">Read More..</a>
    </article>

    <article class="offer" style="left:528px;top:601px">
      <div class="ring"><div class="photo" role="img" aria-label="Slit lamp fitted with a clear breath shield" style="background:radial-gradient(circle,#9a9a9a,#6f5f55 75%)"></div></div>
      <div class="badge"><span>Only</span><span>17.00</span></div>
      <h3>Slit Lamp Breath Shield XL</h3>
      <p>Lorem ipsum is a placeholder<br>text commonly used to...</p>
      <a class="more">Read More..</a>
    </article>
  </section>

  <section class="abs other-services">
    <h4>Our Other Services</h4>
    <ul class="tick-list">
      <li><svg><use href="#tick"/></svg>Preventative Maintenance</li>
      <li><svg><use href="#tick"/></svg>Practice Moving</li>
      <li><svg><use href="#tick"/></svg>Office Relocation Consulting</li>
      <li><svg><use href="#tick"/></svg>Layout Strategy and Equipment</li>
      <li><svg><use href="#tick"/></svg>Set Up Solutions.</li>
    </ul>
  </section>

  <section class="abs brands">
    <h4>We service all major brands such as</h4>
    <ul class="tick-list">
      <li><svg><use href="#tick"/></svg>Vell Dorran</li>
      <li><svg><use href="#tick"/></svg>Tilsa</li>
      <li><svg><use href="#tick"/></svg>Quaven</li>
      <li><svg><use href="#tick"/></svg>Fendworth</li>
      <li><svg><use href="#tick"/></svg>Ulmbrook</li>
      <li><svg><use href="#tick"/></svg>Parsivel</li>
      <li><svg><use href="#tick"/></svg>Kessig and more.</li>
    </ul>
  </section>

  <footer class="abs footer">
    <div class="location">
      <b>Store Location :</b><br>
      Brightfield Optic Services, Inc.<br>
      418 Larkmoor Ave. Halden Park, IL 60099<br>
      <b>Tel. 555-014-2286</b><br>
      <b>E-mail: info@brightfieldoptic.example</b>
    </div>
    <div class="timing">
      <b>Our Timing :</b><br>
      Monday - Friday: 10AM - 5PM<br>
      Saturday: By Appointment<br>
      Sunday: By Appointment<br>
      All Holiday
    </div>
  </footer>

  <div class="abs copyright">© Brightfield Optic Services, Inc.</div>
</main>
</body>
</html>
```